Biz Card Physical Therapy Company
Lorimer Physical Therapy
Bright & Fun-filled
Darnell Okoro, PT, CIMT, CSCS
Director
4172 W Fenwick Ave,
Signal Hill, CA 90755
LorimerTherapy@quillpost.com
CA PT 61803
Please feel free to move the logo to the side of the tag-line, or however you may see fit
vector logo file

```html
<!DOCTYPE html>
<html lang="en">
<head>
<meta charset="utf-8">
<title>Lorimer Physical Therapy – Business Card</title>
<link rel="stylesheet" href="https://fonts.googleapis.com/css2?family=Open+Sans:wght@400;600;700;800&family=Lora:ital@1&display=swap">
<style>
  :root {
    --bg: #e9eaec;
    --card: #ffffff;
    --card-shade: #eef0f1;
    --green: #3f8a1f;
    --green-dark: #2f6c14;
    --green-light: #8fb86d;
    --band: #c9d3c2;
    --text: #5a5f63;
    --muted: #8a8f93;
    --purple-soft: #dccbe6;
  }
  * { box-sizing: border-box; margin: 0; padding: 0; }
  html, body { width: 1200px; height: 901px; overflow: hidden; }
  body {
    background: var(--bg);
    font-family: "Open Sans", sans-serif;
    position: relative;
  }
  .card {
    position: absolute;
    left: 250px;
    width: 700px;
    height: 400px;
    border-radius: 28px;
    overflow: hidden;
    background: linear-gradient(135deg, var(--card) 0%, var(--card-shade) 100%);
    box-shadow: 0 6px 22px rgba(0,0,0,.12);
  }
  .card--back { top: 30px; }
  .card--front { top: 466px; }

  .back-decoration {
    position: absolute;
    left: 40px; top: 40px;
    width: 340px; height: 300px;
    border-radius: 12px;
    background: linear-gradient(160deg, var(--purple-soft) 0%, #e4ecde 60%, rgba(255,255,255,0) 100%);
    opacity: .8;
  }

  .bottom-band { position: absolute; left: 0; bottom: 0; width: 700px; height: 80px; }

  .brand {
    position: absolute;
    left: 40px; top: 130px;
    display: flex; align-items: center; gap: 14px;
  }
  .brand-mark { width: 34px; height: 34px; background: var(--green); flex: none; }
  .brand-name {
    font-weight: 800;
    color: var(--green-dark);
    font-size: 27px;
    line-height: 1.1;
    text-transform: uppercase;
    letter-spacing: .5px;
  }
  .tagline {
    position: absolute;
    left: 40px; top: 222px;
    font-family: "Lora", serif;
    font-style: italic;
    font-size: 14.5px;
    color: var(--muted);
    letter-spacing: 1px;
  }
  .divider {
    position: absolute;
    left: 378px; top: 150px;
    width: 1px; height: 160px;
    background: #9aa0a4;
  }
  .contact { position: absolute; left: 396px; top: 148px; color: var(--text); }
  .contact-name { font-weight: 600; color: var(--green); font-size: 16px; }
  .contact-role { font-size: 13px; color: var(--muted); margin-top: 2px; }
  .contact-address { font-size: 13.5px; line-height: 1.45; margin-top: 26px; }
  .contact-lines { margin-top: 12px; font-size: 13.5px; line-height: 1.5; }
  .contact-line { display: flex; align-items: center; gap: 8px; }
  .contact-line svg { width: 12px; height: 12px; flex: none; }
  .contact-line .spacer { width: 12px; flex: none; }
</style>
</head>
<body>

  <section class="card card--back" aria-label="Card back">
    <div class="back-decoration" role="img" aria-label="Faint brand symbol with a running figure as background decoration"></div>
  </section>

  <section class="card card--front" aria-label="Card front">
    <div class="brand">
      <span class="brand-mark"></span>
      <p class="brand-name">Lorimer<br>Physical Therapy</p>
    </div>
    <p class="tagline">Rehabilitation, Fitness &amp; Performance</p>

    <div class="divider"></div>

    <div class="contact">
      <p class="contact-name">Darnell Okoro, PT, CIMT, CSCS</p>
      <p class="contact-role">Director</p>
      <p class="contact-address">4172 W Fenwick Ave,<br>Signal Hill, CA 90755</p>
      <div class="contact-lines">
        <p class="contact-line">
          <svg viewBox="0 0 12 12"><rect x="3" y="0.5" width="6" height="11" rx="1.2" fill="var(--green)"/><rect x="4.2" y="2" width="3.6" height="6" fill="#fff"/></svg>
          (562) 555-0148
        </p>
        <p class="contact-line">
          <svg viewBox="0 0 12 12"><path d="M3 1 L5 3.5 L4 5 Q5 7 7 8 L8.5 7 L11 9 L9.5 11 Q4 10.5 1 3 Z" fill="var(--green)"/></svg>
          (661) 555-0193
        </p>
        <p class="contact-line">
          <svg viewBox="0 0 12 12"><rect x="0.5" y="2" width="11" height="8" rx="1" fill="var(--green)"/><path d="M1 2.5 L6 6.5 L11 2.5" stroke="#fff" stroke-width="1" fill="none"/></svg>
          LorimerTherapy@quillpost.com
        </p>
      </div>
    </div>

    <svg class="bottom-band" viewBox="0 0 700 80" aria-hidden="true">
      <polygon points="0,40 700,22 700,80 0,80" fill="var(--band)"/>
      <polygon points="0,48 420,40 450,80 0,80" fill="var(--green-light)" opacity=".55"/>
      <polygon points="430,40 700,34 700,80 470,80" fill="var(--green)"/>
    </svg>
  </section>

</body>
</html>
```